Urban Music Nightclub DJ Flyer

The flyer is for a night at a San Diego bar called Copper & Lantern. We tend to play C&L that is more on the bassier side of things but still accessible to the ladies.

The flyer colors would be predominately in black and gold. We're going for a slightly sultry look.

- Ornate Gold frame around the picture.

Changes to the picture:

- Supplied photo has an undesirable tile background
- make it grayscale.

The fonts should complement the frame, have a bit of texture and depth.

Flyer should read

C&L (Largest font)
presents (smallest font)
J TOVAH (Large Font)
BRAXLO x DENHOLM (smaller font)

We've included a quick mock up.

We thank you for the many designs that were submitted. We are close to making our final decision.

```html
<!DOCTYPE html>
<html lang="en">
<head>
<meta charset="utf-8">
<title>C&amp;L presents J TOVAH</title>
<link rel="stylesheet" href="https://fonts.googleapis.com/css2?family=Russo+One&family=Michroma&family=Arimo:wght@400&family=Questrial&display=swap">
<style>
  :root {
    --ink: #000000;
    --gold-pale: #fbe6a0;
    --gold-light: #f0c868;
    --gold-mid: #c9962f;
    --gold-deep: #7a4e12;
    --gold-shadow: #3d2606;
    --glow-blue: #1a3cff;
    --white: #ffffff;
  }
  html, body {
    margin: 0;
    padding: 0;
    overflow: hidden;
    background: var(--ink);
  }
  .flyer {
    position: relative;
    width: 856px;
    height: 1200px;
    background: var(--ink);
    overflow: hidden;
    font-family: "Arimo", Arial, sans-serif;
  }
  .gilt-frame {
    position: absolute;
    left: 0;
    top: 0;
    width: 856px;
    height: 1200px;
  }
  .frame-opening {
    position: absolute;
    left: 96px;
    top: 94px;
    width: 672px;
    height: 1026px;
    background: var(--ink);
    overflow: hidden;
  }
  .portrait {
    position: absolute;
    left: 0;
    top: 0;
    width: 672px;
    height: 800px;
  }
  .headline-glow {
    position: absolute;
    left: 60px;
    top: 570px;
    width: 560px;
    height: 230px;
    background: radial-gradient(ellipse at center, rgba(26,60,255,0.85) 0%, rgba(26,60,255,0.35) 40%, rgba(26,60,255,0) 70%);
  }
  .headline {
    position: absolute;
    left: 0;
    top: 598px;
    width: 672px;
    margin: 0;
    text-align: center;
    font-family: "Russo One", Impact, sans-serif;
    font-weight: 400;
    font-size: 134px;
    line-height: 1;
    color: var(--white);
    letter-spacing: 4px;
    text-shadow: 0 0 14px rgba(26,60,255,0.7);
  }
  .headline .amp {
    font-family: "Arimo", Arial, sans-serif;
    font-size: 62px;
    vertical-align: 26px;
    margin: 0 44px;
  }
  .presents {
    position: absolute;
    left: 0;
    top: 728px;
    width: 672px;
    text-align: center;
    color: var(--white);
    font-size: 35px;
    line-height: 1;
  }
  .rule {
    position: absolute;
    height: 2px;
    background: linear-gradient(90deg, rgba(255,255,255,0) 0%, var(--white) 50%, rgba(255,255,255,0) 100%);
  }
  .rule-presents-left { left: 104px; top: 751px; width: 140px; }
  .rule-presents-right { left: 424px; top: 751px; width: 140px; }
  .rule-artist { left: 126px; top: 898px; width: 420px; }
  .artist {
    position: absolute;
    left: 0;
    top: 832px;
    width: 672px;
    margin: 0;
    text-align: center;
    font-family: "Michroma", sans-serif;
    font-weight: 400;
    font-size: 44px;
    line-height: 1;
    letter-spacing: 5px;
    background: linear-gradient(180deg, var(--gold-pale) 0%, var(--gold-light) 45%, var(--gold-mid) 75%, var(--gold-deep) 100%);
    -webkit-background-clip: text;
    background-clip: text;
    color: transparent;
  }
  .labels {
    position: absolute;
    left: 0;
    top: 920px;
    width: 672px;
    margin: 0;
    text-align: center;
    font-family: "Questrial", sans-serif;
    font-size: 32px;
    line-height: 1;
    letter-spacing: 1px;
    color: var(--white);
  }
</style>
</head>
<body>
<main class="flyer">
  <svg class="gilt-frame" width="856" height="1200" viewBox="0 0 856 1200" role="img" aria-label="Carved gilt picture frame">
    <defs>
      <linearGradient id="gilt" x1="0" y1="0" x2="1" y2="1">
        <stop offset="0" stop-color="#f4cf6e"/>
        <stop offset="0.25" stop-color="#b9831f"/>
        <stop offset="0.5" stop-color="#e3b14a"/>
        <stop offset="0.75" stop-color="#9a6614"/>
        <stop offset="1" stop-color="#f0c868"/>
      </linearGradient>
      <linearGradient id="giltCove" x1="1" y1="0" x2="0" y2="1">
        <stop offset="0" stop-color="#6e4410"/>
        <stop offset="0.5" stop-color="#c99335"/>
        <stop offset="1" stop-color="#5a360a"/>
      </linearGradient>
    </defs>
    <rect x="18" y="18" width="820" height="1164" fill="url(#gilt)"/>
    <rect x="24" y="24" width="808" height="1152" fill="none" stroke="#fbe6a0" stroke-width="3"/>
    <rect x="34" y="34" width="788" height="1132" fill="none" stroke="#5a360a" stroke-width="2"/>
    <rect x="50" y="48" width="756" height="1104" fill="url(#giltCove)"/>
    <rect x="50" y="48" width="756" height="1104" fill="none" stroke="#3d2606" stroke-width="3"/>
    <rect x="66" y="64" width="724" height="1072" fill="url(#gilt)"/>
    <rect x="70" y="68" width="716" height="1064" fill="none" stroke="#fbe6a0" stroke-width="2"/>
    <rect x="84" y="82" width="696" height="1050" fill="url(#giltCove)"/>
    <rect x="92" y="90" width="680" height="1034" fill="none" stroke="#3d2606" stroke-width="4"/>
  </svg>
  <section class="frame-opening">
    <svg class="portrait" width="672" height="800" viewBox="0 0 672 800" role="img" aria-label="Grayscale photo of the artist in a white tank top with arms raised, over a swirling gold backdrop">
      <defs>
        <radialGradient id="backdrop" gradientUnits="userSpaceOnUse" cx="334" cy="430" r="420" gradientTransform="translate(334 430) scale(0.8 1) translate(-334 -430)">
          <stop offset="0" stop-color="#e2e2e2"/>
          <stop offset="0.3" stop-color="#a8a8a8"/>
          <stop offset="0.45" stop-color="#8a6a1c"/>
          <stop offset="0.7" stop-color="#6b4a0e"/>
          <stop offset="1" stop-color="#000000"/>
        </radialGradient>
      </defs>
      <polygon points="0,0 672,0 672,426 334,791 0,486" fill="url(#backdrop)"/>
    </svg>
    <div class="headline-glow"></div>
    <h1 class="headline">C<span class="amp">&amp;</span>L</h1>
    <div class="rule rule-presents-left"></div>
    <div class="presents">presents</div>
    <div class="rule rule-presents-right"></div>
    <h2 class="artist">J TOVAH</h2>
    <div class="rule rule-artist"></div>
    <p class="labels">BRAXLO x DENHOLM</p>
  </section>
</main>
</body>
</html>
```